Background for casino website

We need a background for our casino website.. atm u see in the background of our new site a pic of the marvessa in Vegas.. but we want something unique for us..
What do we offer to our customers.. dicegames, diceslots, videopoker, videoroulette, horsebetting, blackjack.
It needs to look professional(not childish) and it needs to match with the website itself(see attachment)
Good luck and surprise us:)

```html
<!DOCTYPE html>
<html lang="en">
<head>
<meta charset="utf-8">
<title>Marvessa Casino</title>
<link href="https://fonts.googleapis.com/css2?family=Arimo:wght@400;700&family=Marcellus&display=swap" rel="stylesheet">
<style>
:root{
  --red-deep:#5a0508;
  --red:#b10f14;
  --red-bright:#d8161c;
  --red-dark:#2a0203;
  --black:#121010;
  --panel:#1b1818;
  --gold:#e3a21a;
  --gold-light:#f6c64a;
  --green:#1f7a3c;
  --green-dark:#0d3f1e;
  --grey:#8d8d8d;
  --white:#ffffff;
  --display:"Marcellus", serif;
  --body:"Arimo", sans-serif;
}
*{box-sizing:border-box;margin:0;padding:0}
html,body{width:1200px;height:1190px;overflow:hidden}
body{background:var(--red-dark);font-family:var(--body);color:var(--white);position:relative}
.backdrop{position:absolute;top:0;height:1190px;width:296px;
  background:radial-gradient(ellipse at 50% 10%,#e8464a 0%,transparent 35%),
  linear-gradient(180deg,#b31116 0%,#7e070b 40%,#c2171c 70%,#5d0406 100%)}
.backdrop.left{left:0}
.backdrop.right{right:0}
.site{position:absolute;left:296px;top:0;width:610px;height:1190px;background:var(--black);box-shadow:0 0 30px #000}
.site > section,.site > nav,.site > header,.site > footer{position:absolute;left:0;width:610px}

.topbar{top:0;height:19px;background:linear-gradient(#c8151a,#7c0609);display:flex;align-items:center;padding:0 8px;gap:5px}
.flag{width:11px;height:8px;background:linear-gradient(90deg,#1d3b9a 33%,#fff 33% 66%,#d21 66%)}
.flag.nl{background:linear-gradient(#d21 33%,#fff 33% 66%,#1d3b9a 66%)}
.flag.uk{background:#233e8b;border:1px solid #fff}
.topbar .domain{font-size:10px;font-weight:700;margin-left:6px}
.topbar .tagline{margin-left:auto;font-size:10px;font-weight:700}

.masthead{top:19px;height:101px;background:linear-gradient(180deg,#3c3530,#1a1715)}
.brand{position:absolute;left:8px;top:14px;font-family:var(--display);font-size:34px;color:var(--white);display:flex;align-items:center;gap:10px}
.brand .dot{width:16px;height:16px;border-radius:50%;background:var(--gold)}
.login{position:absolute;right:6px;top:18px;width:240px;font-size:8px}
.login .row{display:flex;gap:4px;align-items:center;justify-content:flex-end;margin-bottom:8px}
.login input{width:74px;height:13px;font-size:6.5px;border:1px solid #888;padding:0 3px;font-family:var(--body)}
.btn-gold{background:linear-gradient(#f7b73a,#c8780d);color:var(--white);font-weight:700;font-size:9px;padding:2px 8px;border-radius:2px}
.login .box{width:9px;height:9px;background:var(--white);display:inline-block;vertical-align:middle;margin-right:3px}
.login .signup{color:var(--gold-light);font-weight:700}
.livechat{position:absolute;right:6px;top:63px;width:100px;height:33px;background:var(--white);border-radius:5px;color:#222;padding:5px 6px;display:flex;justify-content:space-between}
.livechat b{font-size:11px;display:block}
.livechat small{font-size:7px}
.livechat .agent{width:26px;height:24px;border-radius:3px;background:linear-gradient(#f0d0b8,#c08a6a)}

.mainnav{top:120px;height:38px;display:flex;background:linear-gradient(#d4181d,#8c080c)}
.mainnav a,.footnav a{flex:1;display:flex;align-items:center;justify-content:center;color:var(--white);text-decoration:none;font-family:var(--display);font-size:11px;border-right:1px solid #5a0306}
.mainnav a.active{background:linear-gradient(#f2b53c,#c07810);color:#3a1d00}

.hero{top:158px;height:203px;background:linear-gradient(100deg,#1a1208 0%,#6e5224 40%,#4a3a22 62%,#262322 80%,#141212 100%)}

.promos{top:361px;height:102px;background:var(--gold);display:flex;gap:10px;padding:5px 6px}
.promo{flex:1;position:relative;background:linear-gradient(#2a9a4c,var(--green-dark));border:2px solid #0c2e16;display:flex;align-items:center;justify-content:center;font-family:var(--display);font-size:20px;text-align:center;line-height:1.1;padding-bottom:10px}
.promo .more{position:absolute;right:3px;bottom:3px;background:linear-gradient(#d9171c,#7e0609);font-size:9px;padding:1px 6px;font-family:var(--body);font-weight:700}

.games{top:463px;height:204px;display:flex}
.games .catalogue{width:407px;background:#0d0b0b;border-right:2px solid #2b2b2b}
.tabs{display:flex;height:21px;background:linear-gradient(#3a3a3a,#151515)}
.tabs a{flex:1;font-family:var(--display);font-size:8.5px;color:var(--white);display:flex;align-items:center;justify-content:center;border-right:1px solid #000;text-decoration:none}
.tabs a.active{color:var(--gold-light);border-bottom:2px solid var(--gold)}
.grid{display:grid;grid-template-columns:repeat(3,1fr);gap:5px 4px;padding:4px 4px 0}
.game{height:76px;display:flex;flex-direction:column;background:#222}
.game .thumb{flex:1}
.game .modes{display:flex;height:11px;font-size:7px;font-weight:700}
.game .modes span{flex:1;display:flex;align-items:center;justify-content:center}
.game .modes .real{background:var(--red)}
.game .modes .practice{background:#444}
.pager{text-align:right;font-size:7.5px;padding:3px 8px}
.games .jackpot{flex:1;background:#0f0d0d;padding:8px}
.jackpot .title{font-family:var(--display);font-size:15px;text-align:center;color:var(--white);margin-top:8px}
.jackpot .amount{font-family:var(--display);font-size:20px;text-align:center;color:var(--white);margin:6px 0 22px}
.winners{height:84px;border:3px solid var(--gold);border-radius:6px;background:#2a2a2a;display:flex;gap:3px;padding:8px 14px 8px 5px;position:relative}
.winners .slot{flex:1;background:var(--white);color:#111;font-size:7.5px;font-weight:700;text-align:center;padding-top:6px}
.winners .slot em{display:block;color:var(--red);font-style:normal;margin-top:3px}
.winners .lever{position:absolute;right:2px;top:8px;width:4px;height:44px;background:#999}
.winners .lever::before{content:"";position:absolute;top:-6px;left:-3px;width:10px;height:10px;border-radius:50%;background:var(--red-bright)}

.content{top:667px;height:457px;background:linear-gradient(180deg,#a30c11 0%,#d3161b 35%,#9a0a0e 100%)}
.content .toggle{position:absolute;right:6px;top:6px;width:11px;height:11px;border-radius:50%;background:var(--gold)}
.content h1{position:absolute;left:200px;top:25px;font-size:15px;font-weight:700}
.content .feature{position:absolute;left:17px;top:55px;width:160px;height:123px;background:linear-gradient(#6a0509,#2a0203)}
.content .intro{position:absolute;left:204px;top:62px;width:400px;font-size:8.5px;line-height:1.3}
.intro p{margin-bottom:9px}
.news{position:absolute;left:21px;top:202px;width:160px;height:245px;background:var(--panel);border-radius:4px;padding:8px 8px}
.news h2{font-size:11px;margin-bottom:8px}
.news li{list-style:none;border-top:1px solid #333;padding:5px 0;display:grid;grid-template-columns:22px 1fr;font-size:8px;line-height:1.25;height:45px}
.news li b{font-size:13px}
.news li em{font-style:normal;color:var(--red-bright);grid-column:2;text-align:right}
.news .all{font-size:8px;text-align:center;margin-top:6px;font-weight:700}
.trust{position:absolute;left:205px;top:210px;width:210px;text-align:center}
.trust .seal{width:30px;height:30px;border-radius:50%;background:#c54a4e;margin:0 auto 24px}
.trust .badges{display:flex;justify-content:center;gap:4px}
.trust .badges span{width:16px;height:16px;border-radius:50%;background:var(--white)}
.trust .badges span:nth-child(2){background:var(--gold)}
.trust .legal{font-size:9px;font-weight:700;margin-top:10px}
.trust svg{margin-top:54px}
.trust .secure{font-size:10px;margin-top:6px}
.media{position:absolute;left:430px;top:202px;width:160px;height:245px;background:var(--panel);border-radius:4px;padding:8px}
.media h2{font-size:11px;margin-bottom:10px}
.media .video{height:90px;background:linear-gradient(#3a3a4a,#0f0f16)}
.media p{font-size:8px;line-height:1.35;margin-top:10px}

.footnav{top:1124px;height:20px;display:flex;background:linear-gradient(#3a3a3a,#111)}
.footnav a{font-size:8px;border-right:1px solid #555}
.basebar{top:1144px;height:46px;background:linear-gradient(#c3151a,#7a0609);display:flex;align-items:center;padding:0 8px;gap:16px}
.card{width:30px;height:19px;border-radius:2px;background:var(--white)}
.basebar .copy{margin-left:auto;font-size:10px;font-weight:700}
</style>
</head>
<body>
<div class="backdrop left" role="img" aria-label="Red casino backdrop with stage light rays, a jockey on a racing horse, two aces and a roulette wheel"></div>
<div class="backdrop right" role="img" aria-label="Red casino backdrop with stage light rays, a jockey on a racing horse, two aces and a roulette wheel"></div>

<main class="site">
  <header class="topbar">
    <span class="flag nl"></span><span class="flag"></span><span class="flag uk"></span>
    <span class="domain">marvessa-casino.net</span>
    <span class="tagline">Play responsibly</span>
  </header>

  <header class="masthead">
    <div class="brand"><span class="dot"></span>Marvessa</div>
    <form class="login">
      <div class="row"><input placeholder="Username or email"><input placeholder="Password"><span class="btn-gold">SIGN IN</span></div>
      <div class="row"><span><span class="box"></span>Remember me</span><span>Forgot password ?</span><span class="signup">SIGN UP NOW</span></div>
    </form>
    <div class="livechat"><div><b>LIVE CHAT</b><small>Need some help ?</small></div><span class="agent" role="img" aria-label="Support agent photo"></span></div>
  </header>

  <nav class="mainnav">
    <a class="active">HOME</a><a>PROMO</a><a>MOBILE CASINO</a><a>GAMING INFOS</a><a>FAQ</a><a>CONTACT US</a>
  </nav>

  <section class="hero" role="img" aria-label="Photo of a stack of black and gold casino chips on a golden table"></section>

  <section class="promos">
    <div class="promo" role="img" aria-label="Promo card with casino chips on green felt">PROMO<br>N°1<span class="more">MORE INFO</span></div>
    <div class="promo" role="img" aria-label="Promo card with casino chips on green felt">PROMO<br>N°2<span class="more">MORE INFO</span></div>
    <div class="promo" role="img" aria-label="Promo card with casino chips on green felt">PROMO<br>N°3<span class="more">MORE INFO</span></div>
  </section>

  <section class="games">
    <div class="catalogue">
      <div class="tabs"><a class="active">NEW GAMES</a><a>DICE</a><a>DICE SLOTS</a><a>ROULETTES</a><a>POKER</a><a>BLACK JACK</a></div>
      <div class="grid">
        <div class="game"><div class="thumb" role="img" aria-label="Dice game preview" style="background:linear-gradient(#2a4fa0,#0c1a40)"></div><div class="modes"><span class="real">REAL</span><span class="practice">PRACTICE</span></div></div>
        <div class="game"><div class="thumb" role="img" aria-label="Dice slots preview" style="background:linear-gradient(#c8151a,#4a0204)"></div><div class="modes"><span class="real">REAL</span><span class="practice">PRACTICE</span></div></div>
        <div class="game"><div class="thumb" role="img" aria-label="Roulette preview" style="background:linear-gradient(#d8a030,#6a3a08)"></div><div class="modes"><span class="real">REAL</span><span class="practice">PRACTICE</span></div></div>
        <div class="game"><div class="thumb" role="img" aria-label="Video poker preview" style="background:linear-gradient(#3a6ab0,#10203a)"></div><div class="modes"><span class="real">REAL</span><span class="practice">PRACTICE</span></div></div>
        <div class="game"><div class="thumb" role="img" aria-label="Blackjack preview" style="background:linear-gradient(#d02a2a,#5a0808)"></div><div class="modes"><span class="real">REAL</span><span class="practice">PRACTICE</span></div></div>
        <div class="game"><div class="thumb" role="img" aria-label="Craps table preview" style="background:linear-gradient(#2a8a4a,#0a3018)"></div><div class="modes"><span class="real">REAL</span><span class="practice">PRACTICE</span></div></div>
      </div>
      <div class="pager">&lt;Prev &nbsp;1 &nbsp;2 &nbsp;3 &nbsp;Next &gt;</div>
    </div>
    <aside class="jackpot">
      <div class="title">Jackpot</div>
      <div class="amount">125 480 €</div>
      <div class="winners">
        <div class="slot">Lulu88<em>10 000 €</em></div>
        <div class="slot">Zorro512<em>550 €</em></div>
        <div class="slot">Bastien77<em>1 200 €</em></div>
        <span class="lever"></span>
      </div>
    </aside>
  </section>

  <section class="content">
    <span class="toggle"></span>
    <h1>Welcome to Marvessa Casino</h1>
    <div class="feature" role="img" aria-label="Casino welcome visual"></div>
    <div class="intro">
      <p>Lorem ipsum dolor sit amet, consectetur adipiscing elit. Vestibulum aliquam neque quis augue varius, in sollicitudin mauris pharetra. Nunc eget tincidunt nunc.</p>
      <p>Aenean sit amet lacus at nunc eleifend cursus sit amet volutpat justo. Pellentesque ornare dictum tincidunt. Mauris a rhoncus augue. Aenean sollicitudin ac ante sed euismod. Suspendisse potenti.</p>
      <p>Integer dignissim augue et nisi congue tincidunt. Donec tempus, augue nec placerat condimentum, arcu neque sodales erat, vehicula faucibus diam odio non magna. Nam blandit non augue vitae mollis. Nullam volutpat justo vitae augue bibendum, id pretium augue condimentum. Donec id odio neque. Maecenas elementum sapien ante, non pretium elit pulvinar nec.</p>
    </div>

    <aside class="news">
      <h2>Dernières news</h2>
      <ul>
        <li><b>02</b><span>Nouveau jeu de dés</span><span>sept.</span><em>suite</em></li>
        <li><b>27</b><span>Tournoi de poker</span><span>août</span><em>suite</em></li>
        <li><b>21</b><span>Bonus de bienvenue</span><span>août</span><em>suite</em></li>
        <li><b>14</b><span>Soirée blackjack</span><span>août</span><em>suite</em></li>
      </ul>
      <div class="all">Toutes les news</div>
    </aside>

    <div class="trust">
      <div class="seal"></div>
      <div class="badges"><span></span><span></span><span></span></div>
      <div class="legal">Jeu légal et encadré</div>
      <svg width="44" height="52" viewBox="0 0 44 52" aria-hidden="true">
        <path d="M10 24V15a12 12 0 0 1 24 0v9" fill="none" stroke="#cfcfcf" stroke-width="5"/>
        <rect x="3" y="22" width="38" height="28" rx="4" fill="#d9d9d9"/>
        <circle cx="22" cy="34" r="4" fill="#777"/>
      </svg>
      <div class="secure">Fast &amp; Secure Paiement</div>
    </div>

    <aside class="media">
      <h2>Vidéo du mois</h2>
      <div class="video" role="img" aria-label="Video still of a casino table"></div>
      <p>Découvrez nos tables en direct et nos nouveaux jeux vidéo roulette.</p>
    </aside>
  </section>

  <nav class="footnav">
    <a>HOME</a><a>PROMO</a><a>MOBILE CASINO</a><a>GAMING INFOS</a><a>FAQ</a><a>CONTACT US</a><a>GENERAL TERMS</a><a>ABOUT US</a>
  </nav>

  <footer class="basebar">
    <span class="card"></span><span class="card"></span><span class="card"></span><span class="card"></span>
    <span class="copy">© 2024 Marvessa Casino</span>
  </footer>
</main>
</body>
</html>
```